依頼詳細
こだわりはございません!!
デザイン、サイズとも自由な発想でご提案ください。
記載項目
住所、会社名、社長名。記載は裏でも面でもOKです。
希望イメージ
シンプル 複雑
単色 カラフル
暗い 明るい
日常 高級
遊び心 厳粛
未来的 伝統的
女性的 男性的
希望する色
赤系
納品ファイル
• イラストレーター形式 (.ai)
補足説明
http://www.yuzunoto.co.jp/
本日(10/21)、店舗ロゴのaiデータを依頼頂きましたので追加致します。

```html
<!DOCTYPE html>
<html lang="ja">
<head>
<meta charset="utf-8">
<title>新年賀状 2017</title>
<link rel="stylesheet" href="https://fonts.googleapis.com/css2?family=Noto+Sans+JP:wght@500;900&family=Noto+Serif+JP:wght@500;700&family=M+PLUS+Rounded+1c:wght@800&display=swap">
<style>
  :root {
    --red: #c8161d;
    --ink: #3a3a3a;
    --paper: #ffffff;
    --frame: #d9d9d9;
    --blossom: #f3c4cf;
    --blossom-soft: #fbe6eb;
    --broth: #e8c48a;
    --bamboo: #7dbb5a;
  }
  html, body {
    margin: 0;
    padding: 0;
    width: 846px;
    height: 1200px;
    overflow: hidden;
    background: var(--paper);
  }
  .card {
    position: relative;
    width: 846px;
    height: 1200px;
    box-sizing: border-box;
    border: 2px solid var(--frame);
    background: var(--paper);
    overflow: hidden;
  }
  .art { position: absolute; }
  .greeting-grid {
    position: absolute;
    left: 180px;
    top: 178px;
    width: 476px;
    height: 486px;
    display: grid;
    grid-template-columns: 233px 233px;
    grid-template-rows: 238px 238px;
    gap: 10px;
  }
  .greeting-tile {
    background: var(--red);
    color: var(--paper);
    font-family: "Noto Sans JP", sans-serif;
    font-weight: 900;
    font-size: 150px;
    line-height: 1;
    display: flex;
    align-items: center;
    justify-content: center;
  }
  .greeting-tile.tl { border-radius: 40px 0 0 0; padding: 0 20px 26px 0; }
  .greeting-tile.tr { border-radius: 0 40px 0 0; padding: 0 0 26px 20px; }
  .greeting-tile.bl { border-radius: 0 0 0 40px; padding: 26px 20px 0 0; }
  .greeting-tile.br { border-radius: 0 0 40px 0; padding: 26px 0 0 20px; }
  .year {
    position: absolute;
    left: 0;
    width: 846px;
    top: 668px;
    margin: 0;
    text-align: center;
    font-family: "M PLUS Rounded 1c", sans-serif;
    font-weight: 800;
    font-size: 180px;
    line-height: 1;
    color: var(--red);
    letter-spacing: 2px;
  }
  .message {
    position: absolute;
    left: 0;
    width: 846px;
    top: 828px;
    padding-left: 24px;
    box-sizing: border-box;
    text-align: center;
    font-family: "Noto Sans JP", sans-serif;
    font-weight: 500;
    font-size: 19px;
    line-height: 42px;
    color: var(--ink);
  }
  .message p { margin: 0; }
  .shop-name {
    position: absolute;
    left: 100px;
    top: 985px;
    display: flex;
    align-items: center;
    gap: 12px;
    font-family: "Noto Serif JP", serif;
    font-weight: 700;
    font-size: 30px;
    color: var(--red);
  }
  .shop-name .mark {
    width: 18px;
    height: 18px;
    background: var(--red);
  }
  .sender {
    position: absolute;
    left: 368px;
    top: 972px;
    font-family: "Noto Serif JP", serif;
    font-style: normal;
    color: var(--ink);
  }
  .sender .title {
    font-size: 20px;
    font-weight: 500;
    margin: 0 0 6px;
    letter-spacing: 1px;
  }
  .sender .title .name { margin-left: 8px; letter-spacing: 4px; }
  .sender .detail {
    margin: 0;
    font-size: 14px;
    line-height: 23px;
    display: flex;
    align-items: center;
    gap: 6px;
  }
</style>
</head>
<body>
<main class="card">
  <svg class="art blossom-faint" style="left:20px;top:30px" width="240" height="160" role="img" aria-label="淡い桜の花びら模様">
    <ellipse cx="120" cy="80" rx="115" ry="70" fill="var(--blossom-soft)" opacity="0.5"/>
  </svg>
  <svg class="art blossom-left" style="left:48px;top:128px" width="140" height="125" role="img" aria-label="淡いピンクの花のイラスト">
    <ellipse cx="70" cy="62" rx="64" ry="56" fill="var(--blossom)" opacity="0.6"/>
  </svg>
  <svg class="art blossom-faint-right" style="left:580px;top:120px" width="220" height="240" role="img" aria-label="淡い桜の花びら模様">
    <ellipse cx="110" cy="120" rx="105" ry="110" fill="var(--blossom-soft)" opacity="0.45"/>
  </svg>
  <svg class="art rooster" style="left:625px;top:16px" width="125" height="125" role="img" aria-label="酉年のニワトリのイラスト">
    <ellipse cx="62" cy="64" rx="54" ry="56" fill="#f4f0ea"/>
  </svg>

  <div class="greeting-grid">
    <div class="greeting-tile tl">新</div>
    <div class="greeting-tile tr">謹</div>
    <div class="greeting-tile bl">年</div>
    <div class="greeting-tile br">賀</div>
  </div>

  <svg class="art ramen-bowl" style="left:283px;top:352px" width="270" height="140" role="img" aria-label="チャーシューと味玉入りのラーメンの写真">
    <defs>
      <radialGradient id="brothTone" cx="50%" cy="45%" r="60%">
        <stop offset="0%" stop-color="#f2d6a4"/>
        <stop offset="100%" stop-color="var(--broth)"/>
      </radialGradient>
    </defs>
    <ellipse cx="135" cy="70" rx="132" ry="66" fill="#ffffff"/>
    <ellipse cx="135" cy="68" rx="118" ry="56" fill="url(#brothTone)"/>
  </svg>

  <svg class="art bamboo" style="left:616px;top:582px" width="90" height="85" role="img" aria-label="笹の葉のイラスト">
    <ellipse cx="45" cy="42" rx="42" ry="38" fill="var(--bamboo)" opacity="0.75"/>
  </svg>

  <h1 class="year">2017</h1>

  <div class="message">
    <p>皆さまのご健勝とご多幸をお祈りいたします。</p>
    <p>本年もどうぞよろしくお願いいたします。</p>
  </div>

  <div class="shop-name">
    <span class="mark"></span>
    <span>ラーメン柚乃屋</span>
  </div>

  <address class="sender">
    <p class="title">代表取締役<span class="name">山田太郎</span></p>
    <p class="detail">
      <svg width="13" height="13" viewBox="0 0 16 16" aria-hidden="true"><path d="M8 1a5 5 0 0 0-5 5c0 4 5 9 5 9s5-5 5-9a5 5 0 0 0-5-5zm0 7a2 2 0 1 1 0-4 2 2 0 0 1 0 4z" fill="var(--red)"/></svg>
      〒000-0011 東京都ダミー区ダミー1-22-3 ダミービル5F
    </p>
    <p class="detail">
      <svg width="13" height="13" viewBox="0 0 16 16" aria-hidden="true"><path d="M4 1l3 3-2 2c1 2 3 4 5 5l2-2 3 3-2 3C7 15 1 9 1 3z" fill="var(--red)"/></svg>
      000-0000-1234
    </p>
  </address>
</main>
</body>
</html>
```